Geschäftsunterlagen mit vorhandenem Logo
Zielgruppe
- Immobilienmakler.
- Vermietung und Verkauf von Immobilien
- Eigentümer, Bauträger, Hausverwaltungen, Immobilienentwickler, Wohnungsbaugesellschaften, Käufer und Mieter.
Aufgabenstellung
Wir suchen ein neues Design für unsere Geschäftsunterlagen. Es soll dem Betrachter ein gutes Gefühl vermittelt. Es soll seriös, edel und dynamisch wirken, aber auch vertrauensvoll und kompetent.
Wir suchen neue Designs für folgende Unterlagen, das Logo soll hierbei etwas stärker im Vordergrund stehen :
- Visitenkarten ( Text= Logo, mein Name Jonas Brettler, Handynr. und Webseite )
- Briefpapier ( Text= Logo, Firmenname, Adresse, email, Tel-Nr., event. Bankverbindung ) + Briefumschlag ( Din-Lang ) + email-Vorlage ( Logo + Firmenname, Adresse + Telefon )
- Mappe für Unterlagen ( Din A4 )
- Vermietungsschild und Verkaufsschild fürs Objekt ( 1. H=700mm x B=440mm und 2. H=600 x B 1000mm ) Falls die Schilder zu viel sind, lassen Sie die Entwürfe bitte weg. Priorität haben die anderen Unterlagen.
Logo ist vorhanden, die Schrift kann noch variiert werden.
Falls Sie Fragen haben, schreiben Sie uns bitte an.

```html
<!DOCTYPE html>
<html lang="de">
<head>
<meta charset="utf-8">
<title>Brettler Immobilien – Geschäftsausstattung</title>
<link href="https://fonts.googleapis.com/css2?family=Montserrat:wght@400;600;700&family=Arimo:wght@400;700&display=swap" rel="stylesheet">
<style>
  :root {
    --navy: #1f3057;
    --navy-soft: #2a3d68;
    --sky: #5aa9e6;
    --ghost: #7e8aa6;
    --ink: #1f2a44;
    --paper: #ffffff;
    --stage: #ffffff;
  }
  * { box-sizing: border-box; margin: 0; padding: 0; }
  html, body { width: 1200px; height: 1127px; overflow: hidden; background: var(--stage); }
  .stage { position: relative; width: 1200px; height: 1127px; font-family: "Arimo", Arial, sans-serif; color: var(--ink); }

  .piece { position: absolute; background: var(--paper); box-shadow: 7px 9px 10px rgba(0,0,0,.35); overflow: hidden; }
  .piece svg.deco { position: absolute; left: 0; top: 0; }

  .brand { display: flex; align-items: center; gap: 8px; font-family: "Montserrat", sans-serif; font-weight: 600; color: var(--navy); line-height: 1; }
  .brand-dot { border-radius: 50%; border: 4px solid var(--navy); flex: none; }
  .brand-name { display: flex; flex-direction: column; letter-spacing: .02em; }

  /* Business card front */
  .card-front { left: 40px; top: 109px; width: 341px; height: 223px; }
  .card-front .card-brand { position: absolute; left: 14px; top: 60px; width: 150px; flex-direction: column; gap: 6px; text-align: center; }
  .card-front .card-brand .brand-dot { width: 60px; height: 60px; }
  .card-front .card-brand .brand-name { font-size: 15px; gap: 3px; align-items: center; }
  .card-front .card-brand .brand-name span:last-child { font-size: 11px; }
  .card-divider { position: absolute; left: 172px; top: 49px; width: 2px; height: 150px; background: var(--navy); }
  .card-name { position: absolute; left: 181px; top: 54px; font-family: "Montserrat", sans-serif; font-size: 17px; color: var(--navy); letter-spacing: .01em; }
  .card-name b { font-weight: 700; }
  .card-name span { font-weight: 400; }
  .contact-list { list-style: none; }
  .contact-list li { display: flex; align-items: center; color: var(--ink); }
  .contact-icon { flex: none; border-radius: 50%; background: var(--navy); display: flex; align-items: center; justify-content: center; }
  .card-front .contact-list { position: absolute; left: 181px; top: 106px; }
  .card-front .contact-list li { font-size: 9.5px; height: 17.5px; gap: 6px; }
  .card-front .contact-icon { width: 11px; height: 11px; }

  /* Business card back */
  .card-back { left: 40px; top: 501px; width: 341px; height: 222px; background: var(--navy); }
  .card-back .frame { position: absolute; inset: 12px; border: 1px solid rgba(255,255,255,.35); }
  .card-back .brand { position: absolute; left: 56px; top: 76px; color: var(--ghost); gap: 10px; }
  .card-back .brand-dot { width: 62px; height: 62px; border-color: var(--ghost); }
  .card-back .brand-name { font-size: 34px; }
  .card-back .brand-name span:last-child { font-size: 20px; font-weight: 600; margin-top: 2px; letter-spacing: .05em; }

  /* Standalone logo */
  .logo-solo { position: absolute; left: 78px; top: 900px; gap: 10px; }
  .logo-solo .brand-dot { width: 76px; height: 76px; border-width: 5px; }
  .logo-solo .brand-name { font-size: 36px; }
  .logo-solo .brand-name span:last-child { font-size: 23px; letter-spacing: .04em; margin-top: 2px; }

  /* Letterhead */
  .letterhead { left: 421px; top: 106px; width: 666px; height: 942px; }
  .letter-brand { position: absolute; left: 452px; top: 56px; gap: 6px; }
  .letter-brand .brand-dot { width: 48px; height: 48px; }
  .letter-brand .brand-name { font-size: 22px; }
  .letter-brand .brand-name span:last-child { font-size: 14px; margin-top: 1px; letter-spacing: .04em; }
  .bank { position: absolute; left: 504px; top: 118px; font-family: "Montserrat", sans-serif; font-size: 12.5px; color: var(--navy); line-height: 17px; }
  .subject { position: absolute; left: 80px; top: 208px; font-size: 12px; color: var(--navy); }
  .body { position: absolute; left: 80px; top: 250px; width: 492px; font-size: 10.4px; line-height: 20.6px; color: #111; }
  .body p + p { margin-top: 7px; }
  .signature { position: absolute; left: 80px; top: 666px; width: 170px; height: 80px; background: linear-gradient(90deg, rgba(31,48,87,.08), rgba(31,48,87,.02)); }
  .signature-label { position: absolute; left: 80px; top: 752px; font-size: 12px; color: var(--navy); }
  .letterhead .contact-list { position: absolute; left: 60px; top: 797px; }
  .letterhead .contact-list li { font-size: 12px; height: 24.5px; gap: 8px; color: var(--navy); }
  .letterhead .contact-icon { width: 16px; height: 16px; }
</style>
</head>
<body>
<main class="stage">

  <!-- Business card front -->
  <section class="piece card-front" aria-label="Visitenkarte Vorderseite">
    <svg class="deco" width="341" height="223" viewBox="0 0 341 223" aria-hidden="true">
      <defs>
        <linearGradient id="cardSky" x1="0" x2="1" y1="0" y2="0">
          <stop offset="0" stop-color="#ffffff"/>
          <stop offset=".55" stop-color="#5aa9e6"/>
          <stop offset="1" stop-color="#5aa9e6"/>
        </linearGradient>
      </defs>
      <path d="M0 0 H341 V20 C240 22 90 42 0 76 Z" fill="url(#cardSky)"/>
      <path d="M0 0 H341 V8 C240 10 90 28 0 66 Z" fill="#1f3057"/>
    </svg>
    <div class="brand card-brand">
      <span class="brand-dot"></span>
      <span class="brand-name"><span>BRETTLER</span><span>IMMOBILIEN</span></span>
    </div>
    <div class="card-divider"></div>
    <h1 class="card-name"><b>JONAS</b> <span>BRETTLER</span></h1>
    <ul class="contact-list">
      <li><span class="contact-icon"><svg width="6" height="7" viewBox="0 0 6 7"><path d="M3 0a2.4 2.4 0 0 0-2.4 2.4C.6 4.2 3 7 3 7s2.4-2.8 2.4-4.6A2.4 2.4 0 0 0 3 0z" fill="#fff"/></svg></span>lindenweg 12 104567 wien</li>
      <li><span class="contact-icon"><svg width="6" height="6" viewBox="0 0 6 6"><path d="M1 0h1.3l.6 1.6-.8.6a3.6 3.6 0 0 0 1.7 1.7l.6-.8L6 3.7V5a1 1 0 0 1-1 1A5 5 0 0 1 0 1a1 1 0 0 1 1-1z" fill="#fff"/></svg></span>+49 151 987 654</li>
      <li><span class="contact-icon"><svg width="6" height="6" viewBox="0 0 6 6"><path d="M0 2.6 6 0 4.2 6 3 3.6z" fill="#fff"/></svg></span>brettler@brettler-immo.de</li>
      <li><span class="contact-icon"><svg width="7" height="7" viewBox="0 0 7 7"><circle cx="3.5" cy="3.5" r="2.5" fill="none" stroke="#fff" stroke-width="1"/></svg></span>www.brettler-immo.de</li>
    </ul>
  </section>

  <!-- Business card back -->
  <section class="piece card-back" aria-label="Visitenkarte Rückseite">
    <div class="frame"></div>
    <div class="brand">
      <span class="brand-dot"></span>
      <span class="brand-name"><span>BRETTLER</span><span>IMMOBILIEN</span></span>
    </div>
  </section>

  <!-- Logo lockup -->
  <div class="brand logo-solo" aria-label="Brettler Immobilien">
    <span class="brand-dot"></span>
    <span class="brand-name"><span>BRETTLER</span><span>IMMOBILIEN</span></span>
  </div>

  <!-- Letterhead -->
  <section class="piece letterhead" aria-label="Briefpapier">
    <svg class="deco" width="666" height="942" viewBox="0 0 666 942" aria-hidden="true">
      <defs>
        <linearGradient id="sheetSkyTop" x1="0" x2="1" y1="0" y2="0">
          <stop offset="0" stop-color="#ffffff"/>
          <stop offset=".5" stop-color="#7bb8ea"/>
          <stop offset="1" stop-color="#5aa9e6"/>
        </linearGradient>
        <linearGradient id="sheetSkyBottom" x1="0" x2="1" y1="0" y2="0">
          <stop offset="0" stop-color="#5aa9e6"/>
          <stop offset=".6" stop-color="#3f7fc0"/>
          <stop offset="1" stop-color="#1f3057"/>
        </linearGradient>
      </defs>
      <path d="M0 0 H666 V34 C450 50 160 92 0 196 Z" fill="url(#sheetSkyTop)"/>
      <path d="M0 0 H666 V20 C450 34 150 76 0 184 Z" fill="#1f3057"/>
      <path d="M0 942 V895 C220 910 500 880 666 760 V942 Z" fill="url(#sheetSkyBottom)"/>
      <path d="M40 942 C300 930 560 870 666 738 V942 Z" fill="#1f3057"/>
    </svg>

    <div class="brand letter-brand">
      <span class="brand-dot"></span>
      <span class="brand-name"><span>BRETTLER</span><span>IMMOBILIEN</span></span>
    </div>
    <div class="bank">IBAN DE9876543210<br>PIC&nbsp;&nbsp;987654321</div>

    <p class="subject">Subject Line: Loreum ipsum dolor sit amet.</p>
    <div class="body">
      <p>Lorem ipsum dolor sit amet, consectetur adipiscing elit. Maecenas at dapibus diam. Vivamus fringilla nulla lorem, sit amet mollis nisi suscipit in. Donec lacus tortor, finibus eget pharetra vitae, auctor eget augue. Mauris euismod libero ac risus fermentum, sed rhoncus erat consectetur. Phasellus eget hendrerit ligula, id volutpat tellus. Praesent viverra sapien at convallis eleifend. Pellentesque ac ipsum felis. Vestibulum augue massa, blandit eu tellus eu, fringilla volutpat quam.</p>
      <p>Nulla in neque sit amet diam lobortis lacinia. Donec tristique tristique ex in fermentum. Donec tristique erat non turpis sollicitudin, et posuere dui congue. Nulla elementum finibus orci, in varius ligula feugiat ut. Donec viverra hendrerit est, quis pulvinar metus pretium et. Lorem ipsum dolor sit amet, consectetur adipiscing elit. Nulla tempus pretium convallis. Nunc imperdiet tempus sem sit amet rutrum. Morbi tempus in lacus sed sollicitudin. Praesent non sem commodo, faucibus metus id, imperdiet odio. Morbi sodales convallis nulla a rutrum. Class aptent taciti sociosqu ad litora torquent per conubia nostra, per inceptos himenaeos. Nulla condimentum iaculis tellus non scelerisque. Fusce lobortis gravida pretium.</p>
      <p>Cras nec quam mauris. Nulla eu urna eu tortor bibendum eleifend. Nulla imperdiet semper ex, ac iaculis massa consequat eget. Maecenas quis dui varius, tincidunt massa vitae, condimentum lacus. Aliquam in viverra lorem. Integer eros tortor, tristique ac quam in, tempor accumsan lectus. Nulla in neque tellus.</p>
    </div>
    <div class="signature" role="img" aria-label="Handschriftliche Unterschrift"></div>
    <p class="signature-label">Signature</p>

    <ul class="contact-list">
      <li><span class="contact-icon"><svg width="8" height="10" viewBox="0 0 6 7"><path d="M3 0a2.4 2.4 0 0 0-2.4 2.4C.6 4.2 3 7 3 7s2.4-2.8 2.4-4.6A2.4 2.4 0 0 0 3 0z" fill="#fff"/></svg></span>lindenweg 12 104567 wien</li>
      <li><span class="contact-icon"><svg width="9" height="9" viewBox="0 0 6 6"><path d="M1 0h1.3l.6 1.6-.8.6a3.6 3.6 0 0 0 1.7 1.7l.6-.8L6 3.7V5a1 1 0 0 1-1 1A5 5 0 0 1 0 1a1 1 0 0 1 1-1z" fill="#fff"/></svg></span>+49 151 987 654</li>
      <li><span class="contact-icon"><svg width="9" height="9" viewBox="0 0 6 6"><path d="M0 2.6 6 0 4.2 6 3 3.6z" fill="#fff"/></svg></span>brettler@brettler-immo.de</li>
      <li><span class="contact-icon"><svg width="10" height="10" viewBox="0 0 7 7"><circle cx="3.5" cy="3.5" r="2.5" fill="none" stroke="#fff" stroke-width="1"/></svg></span>www.brettler-immo.de</li>
    </ul>
  </section>

</main>
</body>
</html>
```